Virtual Assistant/Online Marketing Business Card/Stationary

I need a professional but modern business card/stationary for my company in Dallas called Brivolo. Brivolo is a virtual assistant specializing in online marketing. I would like a unique design that stands out and makes my brand clear. Incorporating the logo is a must and have attached it to this brief.

Target Market(s)

small business owners & entrepreneurs, 35-65

Industry/Entity Type

Business

Contact Information for Business Card

Maren Tolk
marentolk@brivolo.biz
(555) 271-9064
brivolo.biz

Font styles to use
Sans Serif

Colors
f04a50
3176b5
9bcb3c

Requirements
Must have
• Colors that match the logo colors. Logo integration

```html
<!DOCTYPE html>
<html lang="en">
<head>
<meta charset="utf-8">
<title>Brivolo – Business Card</title>
<link rel="stylesheet" href="https://fonts.googleapis.com/css2?family=Open+Sans:ital,wght@0,600;0,700;1,400&family=Roboto:wght@400&display=swap">
<style>
  :root {
    --page-bg: #e9e6e1;
    --card-bg: #f4f2ee;
    --card-edge: #d9d5ce;
    --ink: #2f3133;
    --ink-soft: #4a4c4f;
    --brand-red: #f04a50;
    --brand-blue: #3176b5;
    --brand-green: #9bcb3c;
    --band-blue: #5a8fae;
    --band-dark: #2d2f31;
    --url-tan: #d9c8a6;
    --divider: #dcd8d1;
  }
  * { box-sizing: border-box; margin: 0; padding: 0; }
  html, body { width: 1200px; height: 1200px; overflow: hidden; }
  body {
    background: var(--page-bg);
    position: relative;
    font-family: "Roboto", Arial, sans-serif;
  }
  .business-card {
    position: absolute;
    left: 84px;
    top: 294px;
    width: 1032px;
    height: 612px;
    background: var(--card-bg);
    border: 1px solid var(--card-edge);
    overflow: hidden;
    box-shadow: 0 18px 40px rgba(0,0,0,0.12);
  }
  .card-divider {
    position: absolute;
    left: 546px;
    top: 0;
    width: 1px;
    height: 534px;
    background: var(--divider);
  }
  .brand-mark {
    position: absolute;
    left: 96px;
    top: 250px;
    display: flex;
    align-items: center;
    gap: 18px;
  }
  .brand-dot {
    width: 34px;
    height: 34px;
    border-radius: 50%;
    background: var(--brand-red);
  }
  .brand-name {
    font-family: "Open Sans", Arial, sans-serif;
    font-weight: 700;
    font-size: 84px;
    line-height: 1;
    color: var(--ink);
    letter-spacing: -1px;
  }
  .contact-block {
    position: absolute;
    left: 600px;
    top: 178px;
  }
  .person-name {
    font-family: "Open Sans", Arial, sans-serif;
    font-weight: 600;
    font-size: 41px;
    color: var(--ink);
    line-height: 1.1;
  }
  .person-title {
    font-family: "Open Sans", Arial, sans-serif;
    font-style: italic;
    font-weight: 400;
    font-size: 21px;
    color: var(--ink-soft);
    margin-top: 8px;
  }
  .contact-list {
    list-style: none;
    margin-top: 40px;
  }
  .contact-item {
    display: flex;
    align-items: center;
    font-size: 24px;
    color: var(--ink);
    height: 38px;
  }
  .contact-icon {
    width: 24px;
    height: 24px;
    margin-left: 12px;
    margin-right: 28px;
    flex: none;
  }
  .footer-bands {
    position: absolute;
    left: 0;
    bottom: 0;
    width: 1032px;
    height: 78px;
  }
  .website {
    position: absolute;
    left: 600px;
    bottom: 24px;
    font-size: 22px;
    color: var(--url-tan);
    letter-spacing: 0.5px;
  }
</style>
</head>
<body>
  <div class="business-card">
    <div class="brand-mark">
      <span class="brand-dot"></span>
      <span class="brand-name">Brivolo</span>
    </div>

    <div class="card-divider"></div>

    <div class="contact-block">
      <h1 class="person-name">Maren Tolk</h1>
      <p class="person-title">Managing Director</p>
      <ul class="contact-list">
        <li class="contact-item">
          <svg class="contact-icon" viewBox="0 0 24 24" aria-hidden="true">
            <path d="M3 8c0-2 3-4 9-4s9 2 9 4v2h-5V8H8v2H3z" fill="var(--brand-green)"/>
            <path d="M6 11h12l2 9H4z" fill="var(--brand-green)"/>
            <circle cx="12" cy="15.5" r="2.4" fill="var(--card-bg)"/>
          </svg>
          <span>(555) 271-9064</span>
        </li>
        <li class="contact-item">
          <svg class="contact-icon" viewBox="0 0 24 24" aria-hidden="true">
            <rect x="2" y="5" width="20" height="14" fill="#3f9a8a"/>
            <path d="M2 5l10 8 10-8" fill="none" stroke="var(--card-bg)" stroke-width="1.8"/>
            <path d="M2 19l7-6M22 19l-7-6" fill="none" stroke="var(--card-bg)" stroke-width="1.4"/>
          </svg>
          <span>marentolk@brivolo.biz</span>
        </li>
      </ul>
    </div>

    <svg class="footer-bands" viewBox="0 0 1032 78" aria-hidden="true">
      <polygon points="0,42 538,42 516,78 0,78" fill="var(--band-blue)"/>
      <polygon points="546,0 1032,0 1032,78 498,78" fill="var(--band-dark)"/>
    </svg>
    <p class="website">www.brivolo.biz</p>
  </div>
</body>
</html>
```